Need Letterhead and Business Card

I have a logo but i need new letterhead and biz cards. We are a real estate investment firm so we need very professional but also do not want to be old fashioned. We have 3 locations; Singapore, New York and Ponte Vedra Florida. I can provide full addresses if needed. If you have adjustments to our logo you would recommend we are open to them.
I will be putting in a separate project but we also need a template for our own powerpoint slide presentations and website.

Industry/Entity Type

Real Estate

```html
<!DOCTYPE html>
<html lang="en">
<head>
<meta charset="UTF-8">
<title>Arven Business Card</title>
<link rel="stylesheet" href="https://fonts.googleapis.com/css2?family=Marcellus&family=Tenor+Sans&family=Cormorant+Garamond:ital,wght@1,500&display=swap">
<style>
  :root {
    --backdrop: #dcdddf;
    --brand-blue: #14538b;
    --brand-gold: #b8952f;
    --paper: #ffffff;
    --ink-light: #ffffff;
  }
  * { margin: 0; padding: 0; box-sizing: border-box; }
  html, body {
    width: 1200px; height: 1000px; overflow: hidden;
    background: var(--backdrop);
  }
  .canvas { position: relative; width: 1200px; height: 1000px; }
  .card {
    position: absolute; width: 480px; height: 274px;
    box-shadow: 0 3px 10px rgba(0,0,0,0.18);
    overflow: hidden;
  }
  .card-front { left: 170px; top: 170px; background: var(--brand-blue); }
  .card-back { left: 560px; top: 560px; background: var(--paper); }

  .wordmark {
    font-family: "Marcellus", serif;
    letter-spacing: 2px;
    line-height: 1;
  }
  .front-brand {
    position: absolute; left: 0; right: 0; top: 88px;
    text-align: center;
  }
  .front-brand .wordmark { font-size: 60px; color: var(--ink-light); }
  .front-brand .rule {
    width: 200px; height: 2px; background: var(--ink-light);
    margin: 8px auto 5px;
  }
  .tagline {
    font-family: "Tenor Sans", sans-serif;
    color: var(--brand-gold);
    text-transform: uppercase;
    letter-spacing: 0.6px;
  }
  .front-brand .tagline { font-size: 10px; }

  .back-brand { position: absolute; left: 34px; top: 40px; }
  .back-brand .wordmark { font-size: 32px; color: var(--brand-blue); }
  .back-brand .rule { width: 112px; height: 1.5px; background: var(--brand-blue); margin: 4px 0 3px; }
  .back-brand .tagline { font-size: 5.5px; }

  .curve-panel { position: absolute; inset: 0; }

  .holder { position: absolute; left: 300px; top: 66px; }
  .holder-name {
    font-family: "Tenor Sans", sans-serif;
    font-size: 21px; color: var(--ink-light);
  }
  .holder-title {
    font-family: "Cormorant Garamond", serif;
    font-style: italic; font-weight: 500;
    font-size: 15px; color: var(--brand-gold);
  }
  .contact-list {
    position: absolute; left: 318px; top: 128px;
    list-style: none;
    font-family: "Tenor Sans", sans-serif;
    font-size: 11.5px; line-height: 17px; color: var(--ink-light);
  }
  .contact-list .label { color: var(--brand-gold); }
  .office {
    position: absolute; left: 200px; top: 182px;
    font-family: "Tenor Sans", sans-serif;
    font-size: 11.5px; line-height: 16px; color: var(--ink-light);
  }
  .office-name { color: var(--brand-gold); }
</style>
</head>
<body>
<main class="canvas">
  <section class="card card-front" aria-label="Business card front">
    <div class="front-brand">
      <div class="wordmark">ARVEN</div>
      <div class="rule"></div>
      <div class="tagline">Real Estate Investment &amp; Management</div>
    </div>
  </section>

  <section class="card card-back" aria-label="Business card back">
    <svg class="curve-panel" width="480" height="274" viewBox="0 0 480 274" aria-hidden="true">
      <path d="M480,30 C330,30 200,120 150,274 L480,274 Z" fill="var(--brand-blue)"/>
      <path d="M480,30 C330,30 200,120 150,274" fill="none" stroke="var(--brand-gold)" stroke-width="9"/>
    </svg>
    <div class="back-brand">
      <div class="wordmark">ARVEN</div>
      <div class="rule"></div>
      <div class="tagline">Real Estate Investment &amp; Management</div>
    </div>
    <div class="holder">
      <div class="holder-name">Daniel Reyes</div>
      <div class="holder-title">Managing Partner</div>
    </div>
    <ul class="contact-list">
      <li><span class="label">T:</span> 555-0142-7788</li>
      <li><span class="label">E:</span> hello@arven.sg</li>
      <li><span class="label">W:</span> www.arven.sg</li>
    </ul>
    <address class="office" style="font-style:normal">
      <div class="office-name">Singapore Office</div>
      <div>48, Harbour Lane Street,</div>
      <div>Eastville, Postal Code.</div>
    </address>
  </section>
</main>
</body>
</html>
```